Business Card Design Project

Looking to get a new business card design for a 16pt matte finish and spot UV front and back. The designs I'm looking for would be a black background with our logo incorporated somehow and three different color ink swirls/splatters for pink, yellow, blue. a design inspiration would be a card that www.plainvale.net did for his business card.
Updates

I've added some sample cards in my files to show the direction I'd like to go in.

Target Market(s)

upscale automotive industry

Industry/Entity Type

Business

Requirements
Must have
• logo
ink vapor swirl and or splatter in either black or three colors, pink, yellow, blue
Should not have
• normal everyday business card

```html
<!DOCTYPE html>
<html lang="en">
<head>
<meta charset="utf-8">
<title>Kestrel Business Card</title>
<link href="https://fonts.googleapis.com/css2?family=Lato:wght@400;700&display=swap" rel="stylesheet">
<style>
  :root {
    --page-bg: #e6e3de;
    --card-black: #060606;
    --card-grey: #2c2c2c;
    --brand-blue: #1b72c4;
    --ink-navy: #0d3a6a;
    --ghost: #1e1e1e;
    --white: #ffffff;
  }
  * { margin: 0; padding: 0; box-sizing: border-box; }
  html, body {
    width: 1200px; height: 1000px; overflow: hidden;
    background: var(--page-bg);
    font-family: "Lato", Arial, sans-serif;
  }
  .sheet {
    position: relative; width: 1200px; height: 1000px;
    display: flex; align-items: center; justify-content: center; gap: 40px;
  }
  .card {
    position: relative; width: 540px; height: 300px; overflow: hidden;
    background: var(--card-black);
    box-shadow: 0 6px 14px rgba(0,0,0,0.35);
  }
  .card--front {
    background: radial-gradient(ellipse at 50% 48%, var(--card-grey) 0%, #151515 42%, var(--card-black) 80%);
  }
  .brand-name {
    position: absolute; top: 24px; right: 28px;
    font-weight: 700; font-size: 34px; line-height: 1; color: var(--brand-blue);
  }
  .brand-ghost {
    position: absolute; left: 0; right: 0; top: 112px; text-align: center;
    font-weight: 700; font-size: 62px; line-height: 1; color: var(--ghost);
  }
  .holder {
    position: absolute; left: 30px; bottom: 34px; text-align: center;
    color: var(--brand-blue);
  }
  .holder-name { font-weight: 700; font-size: 22px; line-height: 1.2; }
  .holder-role { font-size: 18px; line-height: 1.2; margin-top: 2px; }
  .contact {
    position: absolute; right: 24px; bottom: 30px; text-align: right;
    color: var(--brand-blue); font-size: 16px; line-height: 1.45;
  }
  .ink-splash { position: absolute; inset: 0; width: 100%; height: 100%; display: block; }
  .brand-center {
    position: absolute; left: 0; right: 0; top: 122px; text-align: center;
    font-weight: 700; font-size: 58px; line-height: 1; color: var(--white);
  }
</style>
</head>
<body>
  <main class="sheet">
    <section class="card card--front">
      <div class="brand-name">Kestrel</div>
      <div class="brand-ghost">Kestrel</div>
      <div class="holder">
        <div class="holder-name">Rowan Hale</div>
        <div class="holder-role">manager</div>
      </div>
      <div class="contact">
        <div>Tel: 5550142876</div>
        <div>office@kestrelmoto.com</div>
        <div>www.kestrelmoto.com</div>
      </div>
    </section>
    <section class="card card--back">
      <svg class="ink-splash" viewBox="0 0 540 300" role="img" aria-label="Navy blue ink splatter spreading across a black background">
        <rect width="540" height="300" fill="var(--card-black)"/>
        <ellipse cx="285" cy="155" rx="190" ry="120" fill="var(--ink-navy)"/>
      </svg>
      <div class="brand-center">Kestrel</div>
    </section>
  </main>
</body>
</html>
```